American cannabis tech company business card design

Thrum.com is seeking a modern, professional, and brand-aligned business card that represents our company and its core values: Mission, Story, Values, and Impact. As an innovative cannabis company, we want a business card that is not only visually appealing but also serves as a representation of who we are and what we stand for.

Project Scope: Design a double-sided business card that integrates our brand identity and core values. Incorporate our key brand elements, ensuring a sleek and contemporary aesthetic. Visually reflect our core values (Mission, Story, Values, Impact) in a way that is engaging yet professional.

Target Market(s)

Vendors, third parties,

Contact Information for Business Card

Contact details (name, title, email, phone, website, etc.)

Font styles to use
Other font styles liked:
• Caslon, Centra

Colors

Designer to choose colors to be used in the design.

Requirements
Must have
• Thrum.com logo and branding A creative yet clean way to integrate our core values (Mission, Story, Values, Impact) Modern typography and a well-structured layout
Nice to have
• forest green, grey, white, black
Should not have
• references to marijuana, leafs, plants, or related product

```html
<!DOCTYPE html>
<html lang="en">
<head>
<meta charset="utf-8">
<title>Thrum.com Business Card</title>
<link href="https://fonts.googleapis.com/css2?family=Playfair+Display:wght@700;800&family=Montserrat:wght@400;500&display=swap" rel="stylesheet">
<style>
  :root {
    --forest: #1b3a1f;
    --forest-deep: #132a16;
    --forest-mark: #0f2112;
    --paper: #ffffff;
    --stage: #3a3a3a;
    --ink-soft: #2a2a2a;
  }
  * { margin: 0; padding: 0; box-sizing: border-box; }
  html, body { width: 1200px; height: 875px; overflow: hidden; }
  body {
    background: var(--stage);
    display: flex;
    align-items: center;
    justify-content: center;
    gap: 40px;
  }
  .card {
    width: 540px;
    height: 310px;
    border-radius: 18px;
    position: relative;
    overflow: hidden;
    box-shadow: 0 18px 40px rgba(0,0,0,0.45);
  }
  /* back side */
  .card-back {
    background: var(--forest);
    display: flex;
    align-items: center;
    justify-content: center;
  }
  .card-back .wordmark-large {
    font-family: "Playfair Display", serif;
    font-weight: 800;
    font-size: 120px;
    letter-spacing: -2px;
    color: var(--forest-mark);
  }
  /* front side */
  .card-front { background: var(--paper); }
  .front-body {
    position: absolute;
    left: 0; right: 0; top: 0;
    height: 226px;
    display: flex;
    align-items: center;
    padding-left: 70px;
    padding-top: 30px;
  }
  .wordmark {
    font-family: "Playfair Display", serif;
    font-weight: 800;
    font-size: 48px;
    letter-spacing: -1px;
    color: var(--forest);
    margin-right: 20px;
  }
  .divider {
    width: 1px;
    height: 120px;
    background: var(--forest);
    margin-right: 18px;
  }
  .contact { color: var(--forest); }
  .contact .name {
    font-family: "Playfair Display", serif;
    font-weight: 700;
    font-size: 21px;
    line-height: 1.1;
  }
  .contact .title {
    font-family: "Playfair Display", serif;
    font-weight: 700;
    font-size: 11px;
    margin: 3px 0 10px;
  }
  .contact ul { list-style: none; }
  .contact li {
    font-family: "Montserrat", sans-serif;
    font-size: 13px;
    color: var(--ink-soft);
    display: flex;
    align-items: center;
    gap: 8px;
    margin-bottom: 5px;
  }
  .contact li svg { width: 11px; height: 11px; fill: var(--forest); flex: none; }
  .address-band {
    position: absolute;
    left: 0; right: 0;
    top: 232px;
    height: 48px;
    background: var(--forest);
    color: var(--paper);
    font-family: "Montserrat", sans-serif;
    font-size: 13px;
    display: flex;
    align-items: center;
    padding-left: 150px;
  }
</style>
</head>
<body>
  <section class="card card-back" aria-label="Card back">
    <span class="wordmark-large">THRUM</span>
  </section>

  <section class="card card-front" aria-label="Card front">
    <div class="front-body">
      <span class="wordmark">THRUM</span>
      <span class="divider"></span>
      <div class="contact">
        <p class="name">Daniel Hart</p>
        <p class="title">Owner</p>
        <ul>
          <li>
            <svg viewBox="0 0 24 24"><path d="M6.6 10.8a15 15 0 0 0 6.6 6.6l2.2-2.2a1 1 0 0 1 1-.25 11.4 11.4 0 0 0 3.6.57 1 1 0 0 1 1 1V20a1 1 0 0 1-1 1A17 17 0 0 1 3 4a1 1 0 0 1 1-1h3.5a1 1 0 0 1 1 1c0 1.25.2 2.45.57 3.57a1 1 0 0 1-.25 1z"/></svg>
            555-018-2246
          </li>
          <li>
            <svg viewBox="0 0 24 24"><path d="M2 5h20v14H2z M2 5l10 8 10-8" /><path d="M3 6l9 7 9-7v12H3z" fill="#fff"/></svg>
            info@thrum.com
          </li>
          <li>
            <svg viewBox="0 0 24 24"><circle cx="12" cy="12" r="10"/><path d="M2 12h20M12 2c3 3 3 17 0 20M12 2c-3 3-3 17 0 20" stroke="#fff" stroke-width="1.5" fill="none"/></svg>
            www.thrum.com
          </li>
        </ul>
      </div>
    </div>
    <div class="address-band">418 Linden Ave, #12 Fairbrook, OH 43110</div>
  </section>
</body>
</html>
```